Brookhaven Business Card

I would like to re-design my company business card. I have my main company logo (Brookhaven) which must remain unchanged and I also have a number of product brands which I would like to also show on the card in some way. The corporate company colors are Blue and Orange, see pantone colors on file. However, it is not necessary to use these colors thoroughout. I am ok with grey tones etc...

Target Market(s)

Trade Business

Industry/Entity Type

Furniture

Contact Information for Business Card

Needs to incorporate Brookhaven as the main Logo. The Torvel and Kandrel product brands within the company. These can be on the back of the card.

Font styles to use
Sans Serif

Colors
0355a3
f37122

Requirements
Must have
• Marco Velditch
• COO (Global)
• Brookhaven Pacific Holdings Inc. (4371)
• Level 3, 47 Harlow Street, Melbourne VIC 3000 Australia
• Tel: +61 3 9481 2736 Mobile: +61 427 586 204
• e-mail: marco@brookhaven-au.example
• web: www.brookhaven-au.example
Nice to have
• Should be a corporate
Should not have
• No images of furniture

```html
<!DOCTYPE html>
<html lang="en">
<head>
<meta charset="utf-8">
<title>Brookhaven Business Card</title>
<link rel="stylesheet" href="https://fonts.googleapis.com/css2?family=Roboto:wght@400;500;700&display=swap">
<style>
  :root {
    --brand-blue: #1652e8;
    --brand-orange: #f37122;
    --torvel-green: #58b51f;
    --ink: #1b1b1b;
    --paper: #ffffff;
    --stage: #e9e6e1;
  }
  * { box-sizing: border-box; margin: 0; padding: 0; }
  html, body {
    width: 1200px; height: 1000px; overflow: hidden;
    background: var(--stage);
    font-family: "Roboto", Arial, sans-serif;
  }
  .canvas { position: relative; width: 1200px; height: 1000px; }
  .card {
    position: absolute; width: 560px; height: 320px;
    background: var(--paper); overflow: hidden;
    box-shadow: 0 10px 24px rgba(0,0,0,0.18);
  }
  /* Front: product brand */
  .card--front { left: 90px; top: 90px; }
  .product-brand {
    position: absolute; left: 0; right: 0; top: 100px;
    text-align: center;
  }
  .product-name {
    display: block; font-weight: 700; font-size: 96px; line-height: 1;
    letter-spacing: 2px; color: var(--torvel-green); text-transform: uppercase;
  }
  .product-byline {
    display: block; margin-top: 6px; font-weight: 500; font-size: 30px;
    color: var(--ink); padding-left: 150px;
  }
  /* Back: company contact */
  .card--back { left: 550px; top: 560px; }
  .back-head { height: 150px; display: flex; align-items: center; padding-left: 36px; gap: 26px; }
  .brand-square { width: 70px; height: 70px; background: var(--brand-orange); border-radius: 8px; flex: none; }
  .brand-name { font-weight: 700; font-size: 64px; color: var(--brand-blue); letter-spacing: -1px; }
  .back-band {
    position: absolute; left: 0; right: 0; top: 150px; bottom: 0;
    background: var(--brand-blue); color: var(--paper);
    padding: 20px 36px;
  }
  .contact-name { font-weight: 700; font-size: 18px; color: var(--brand-orange); }
  .contact-title { font-size: 13px; margin-top: 3px; }
  .contact-list { list-style: none; margin-top: 12px; font-size: 13px; line-height: 19px; }
  .contact-list li { display: flex; align-items: center; gap: 10px; }
  .contact-list svg { width: 11px; height: 11px; fill: var(--paper); flex: none; }
  .company-address {
    position: absolute; left: 320px; top: 20px;
    font-size: 13px; line-height: 19px; font-style: normal;
  }
</style>
</head>
<body>
<div class="canvas">

  <section class="card card--front">
    <div class="product-brand">
      <span class="product-name">Torvel</span>
      <span class="product-byline">by Brookhaven</span>
    </div>
  </section>

  <section class="card card--back">
    <header class="back-head">
      <span class="brand-square"></span>
      <span class="brand-name">Brookhaven</span>
    </header>
    <div class="back-band">
      <p class="contact-name">Marco Velditch</p>
      <p class="contact-title">COO (Global)</p>
      <ul class="contact-list">
        <li><svg viewBox="0 0 12 12"><path d="M2.5 1l2 2.3-1 1.2a7 7 0 0 0 4 4l1.2-1 2.3 2-1.2 1.5C5.5 11 1 6.5.9 2.2z"/></svg>+61 3 9481 2736</li>
        <li><svg viewBox="0 0 12 12"><path d="M3 0h6v12H3zM4 1.5v8h4v-8z"/></svg>+61 427 586 204</li>
        <li><svg viewBox="0 0 12 12"><path d="M0 2h12v8H0zM1 3l5 3.5L11 3v-.2H1z"/></svg>marco@brookhaven-au.example</li>
        <li><svg viewBox="0 0 12 12"><path d="M6 0a6 6 0 1 0 0 12A6 6 0 0 0 6 0zm0 1.3c.8 1 1.3 2.5 1.4 4H4.6c.1-1.5.6-3 1.4-4zM1.3 6.7h2.3c.1 1.5.5 2.8 1.1 3.8A4.7 4.7 0 0 1 1.3 6.7zm0-1.4a4.7 4.7 0 0 1 3.4-3.8c-.6 1-1 2.3-1.1 3.8zm3.3 1.4h2.8c-.1 1.5-.6 2.9-1.4 4-.8-1.1-1.3-2.5-1.4-4zm3.8 0h2.3a4.7 4.7 0 0 1-3.4 3.8c.6-1 1-2.3 1.1-3.8zm0-1.4c-.1-1.5-.5-2.8-1.1-3.8a4.7 4.7 0 0 1 3.4 3.8z"/></svg>www.brookhaven-au.example</li>
      </ul>
      <address class="company-address">
        Brookhaven Pacific Holdings Inc. (4371)<br>
        Level 3, 47 Harlow Street, Melbourne<br>
        VIC 3000 Australia
      </address>
    </div>
  </section>

</div>
</body>
</html>
```